Stationery Design Project

We need a stationery design to change our look to a more corporate design. My company has been established since 1989 and over that time has changed from your average sign company to doing more Corporate re branding projects and have some multi National clients.
Our website is currently being redesigned so we need a new logo and business cards etc. to compliment it.
I have 2 graphic designers employed but i want on outsiders opinion and a totally independant view point.
Updates
Hi Designers
We are predominantely a sign manufacturing company that manufacturers every type of sign you can imagine. However the majoprity of our work is digital graphics. Our claim to faim is that we wrap the Harbour Skytrams and Glidetrams which everyone seems to know in Sydney.We also do all sorts of Large format digital printing, vehicle wraps,vinyl signage,LED & Neon Illuminated signage,CNC Routing all materials,Laser cutting and Engraving, Architectural signage, Cut Out letters and Screenprinting.
Aswell as this we totally re-brand companies with internal wall graphics reception signage way finding signage and the like.We are a medium size company that has been trading since 1989 and has some very large reputable clients.
Our Company name is Brightmark Pty Ltd but like to have Signage and Graphics in our stationery.
Our details are as follows T: 9381 5027 F: 9381 5063 Unit 4, 22 Quarry Lane.Pine Flats. NSW 2163 email mail@brightmarkexample.com our current website is being re-designed www.brightmarkexample.com
The design and colour scheme i would like is quite simple with a corporate feel and blue, grey & magenta are colours that seem to suit but am open to most suggestions just looking for clean lines.
Hopefully this is enough information if you require any more please ask.
Regards Neil Barrowby
We are looking to simplify our LOGO not too concerned yet about layout of stationery items that we can easily work on later. I want to get a new logo that we can work with before we return to work on the 16th January so please concentrate on just the logo for now.
We would like to have Signs & Graphics somewhere in the name even though our registered name is Brightmark Pty Ltd. Brightmark is one word, i want it to be quite a bold font with no seriffs.The bright blue and grey colours are favourites so far with maybe a little magenta added later. Would like to have a Logo that is totally seperate and then the Brightmark P/L Signs & graphics as a secondary item just to let people know what Brightmark do as the name obviously does not say what we are about.
Also we need to consider how we can put logo on T-shirts work shirts and company vehicles.
We do not need CD cover or envelopes but letterheads and business cards.
Industry/Entity Type
Business
Look and feel
Each slider illustrates characteristics of the customer's brand and the style your logo design should communicate.

```html
<!DOCTYPE html>
<html lang="en">
<head>
<meta charset="utf-8">
<title>Brightmark Pty Ltd – Business Card</title>
<link rel="stylesheet" href="https://fonts.googleapis.com/css2?family=Open+Sans:wght@400;600;700&display=swap">
<style>
  :root {
    --backdrop: #3b3b3d;
    --card-white: #ffffff;
    --brand-blue: #26a3df;
    --band-blue: #29a3dd;
    --text-white: #ffffff;
    --divider: rgba(255,255,255,0.75);
    --brand-square: #e6398f;
  }
  * { margin: 0; padding: 0; box-sizing: border-box; }
  html, body {
    width: 1200px; height: 534px; overflow: hidden;
    background: var(--backdrop);
    font-family: "Open Sans", Arial, sans-serif;
  }
  .canvas { position: relative; width: 1200px; height: 534px; }

  .card {
    position: absolute; top: 121px;
    width: 511px; height: 291px;
    background: var(--card-white);
    overflow: hidden;
  }
  .card--front { left: 68px; }
  .card--back { left: 621px; }

  /* Front */
  .front-brand {
    position: absolute; left: 0; right: 0; top: 150px;
    display: flex; justify-content: center; align-items: center; gap: 12px;
  }
  .brand-square { width: 18px; height: 18px; background: var(--brand-square); }
  .brand-name {
    font-weight: 700; color: var(--brand-blue);
    font-size: 30px; letter-spacing: 0.5px; line-height: 1;
  }
  .front-url {
    position: absolute; left: 0; right: 0; top: 260px;
    text-align: center; color: var(--brand-blue);
    font-size: 15px; letter-spacing: 3px; font-weight: 600;
  }

  /* Back */
  .back-brand {
    position: absolute; left: 34px; top: 36px;
    display: flex; align-items: center; gap: 10px;
  }
  .back-brand .brand-square { width: 14px; height: 14px; }
  .back-brand .brand-name { font-size: 20px; }

  .info-band {
    position: absolute; left: 0; right: 0; top: 120px; bottom: 0;
    background: var(--band-blue);
  }
  .band-notch {
    position: absolute; left: 58px; top: -12px;
    width: 24px; height: 13px;
  }
  .contact { position: absolute; color: var(--text-white); font-size: 12px; line-height: 20px; }
  .contact--company { left: 42px; top: 36px; }
  .company-name { font-size: 15px; font-weight: 600; line-height: 20px; }
  .contact--address { left: 42px; top: 92px; }
  .divider {
    position: absolute; left: 287px; top: 42px; width: 1px; height: 84px;
    background: var(--divider);
  }
  .contact--lines { left: 298px; top: 37px; }
  .contact--web { left: 298px; top: 92px; }
  .web-url { font-size: 13.5px; font-weight: 600; }
</style>
</head>
<body>
<main class="canvas">
  <section class="card card--front" aria-label="Business card front">
    <div class="front-brand">
      <span class="brand-square"></span>
      <span class="brand-name">Brightmark</span>
    </div>
    <p class="front-url">www.brightmarkexample.com</p>
  </section>

  <section class="card card--back" aria-label="Business card back">
    <div class="back-brand">
      <span class="brand-square"></span>
      <span class="brand-name">Brightmark</span>
    </div>
    <div class="info-band">
      <svg class="band-notch" viewBox="0 0 24 13" aria-hidden="true">
        <polygon points="0,0 24,0 12,13" fill="#ffffff"/>
      </svg>
      <div class="contact contact--company">
        <p class="company-name">Brightmark Pty Ltd</p>
        <p>Position</p>
      </div>
      <div class="contact contact--address">
        <p>Unit 4, 22 Quarry Lane.</p>
        <p>Pine Flats. NSW 2163</p>
      </div>
      <span class="divider"></span>
      <div class="contact contact--lines">
        <p>T: 9381 5027</p>
        <p>F: 9381 5063</p>
      </div>
      <div class="contact contact--web">
        <p>E: mail@brightmarkexample.com</p>
        <p class="web-url">www.brightmarkexample.com</p>
      </div>
    </div>
  </section>
</main>
</body>
</html>
```